Insurance Agency website design for Vell Harbor Insurance, LP

Build a website for Vell Harbor Insurance, LP which sells Homeowners, Auto, Renters, Condo, Flood, Disability, Life, Umbrella, and health insurance. We need the coolest insurance agency website out there to get quotes, contact us, or get additional information. Please list the following insurance companies we work with: Dranko, Lisk, Corvane Mutual, Tremix, Wendmarch, QRZ, and Plumeworth.

Make a design similar to https://www.brimlockagents.example/

Selling personal insurance policies

```html
<!DOCTYPE html>
<html lang="en">
<head>
<meta charset="utf-8">
<title>Vell Harbor Insurance, LP</title>
<link rel="stylesheet" href="https://fonts.googleapis.com/css2?family=Poppins:wght@400;500;600;700;800&family=Lato:wght@400;700&display=swap">
<style>
:root{
  --navy:#0b2a78;
  --navy-deep:#082463;
  --blue:#0a6fb8;
  --topbar:#0a4f96;
  --teal:#1fa58a;
  --teal-dark:#178d76;
  --heading:#0d4a96;
  --text:#1d1d1d;
  --white:#ffffff;
}
*{box-sizing:border-box;margin:0;padding:0}
html,body{width:1200px;height:3675px;overflow:hidden}
body{font-family:'Lato',sans-serif;color:var(--text);background:var(--white);position:relative}

/* top bar */
.topbar{height:50px;background:var(--topbar);color:var(--white);display:flex;align-items:center;gap:32px;padding-left:110px;font-family:'Poppins',sans-serif;font-size:14px}
.topbar span{display:flex;align-items:center;gap:8px}

/* nav */
.nav{height:86px;position:relative;display:flex;align-items:center;padding:0 113px;font-family:'Poppins',sans-serif;font-size:16px}
.nav-links{display:flex;gap:46px;white-space:nowrap}
.nav-links a{color:var(--text);text-decoration:none}
.nav-links a.active{color:var(--teal);text-decoration:underline}
.brand{position:absolute;left:50%;transform:translateX(-50%);display:flex;align-items:center;gap:10px;font-family:'Poppins',sans-serif;font-weight:700;font-size:20px;color:var(--heading);white-space:nowrap}
.brand-mark{width:34px;height:34px;background:var(--heading);flex:none}
.btn-pill{display:inline-flex;align-items:center;justify-content:center;border-radius:30px;font-family:'Poppins',sans-serif;font-weight:600;color:var(--white);text-decoration:none}
.contact-btn{margin-left:auto;background:var(--teal);width:126px;height:42px;font-size:15px;font-weight:500}

/* hero */
.hero{height:289px;background:var(--blue);display:flex;align-items:center;justify-content:center;text-align:center}
.hero h1{font-family:'Poppins',sans-serif;font-weight:600;color:var(--white);font-size:43px;line-height:61px;width:880px}
.split{height:175px;display:flex}
.split-card{flex:1;display:flex;align-items:center;justify-content:center;gap:34px;color:var(--white)}
.split-card.business{background:var(--navy)}
.split-card.personal{background:var(--teal)}
.avatar{width:114px;height:114px;border-radius:50%;border:2px dashed var(--white);padding:5px}
.avatar div{width:100%;height:100%;border-radius:50%}
.split-body{text-align:center;font-family:'Poppins',sans-serif}
.split-body h2{font-size:27px;font-weight:600;margin-bottom:6px}
.split-body p{font-size:11px;font-weight:500;line-height:22px}
.split-body .btn-pill{margin-top:8px;height:38px;padding:0 20px;font-size:14px;border:2px solid var(--white)}
.business .btn-pill{background:var(--teal)}
.personal .btn-pill{background:var(--navy)}
.hero-tail{height:42px;background:var(--blue)}

/* partners */
.partners{height:143px;display:flex;align-items:center;justify-content:space-between;padding:0 70px}
.partner{font-family:'Poppins',sans-serif;font-weight:600;font-size:20px;color:#2a2a2a;white-space:nowrap}

/* about */
.about{position:relative;height:590px;text-align:center}
.dash-right{position:absolute;left:648px;top:47px;width:552px;height:45px;border-top:2px dashed var(--teal);border-left:2px dashed var(--teal)}
.dash-left{position:absolute;left:0;top:589px;width:645px;height:48px;border-top:2px dashed var(--teal);border-right:2px dashed var(--teal)}
.section-title{font-family:'Poppins',sans-serif;font-weight:700;color:var(--heading);font-size:42px}
.about .section-title{padding-top:110px}
.about p{width:870px;margin:20px auto 0;font-size:14.5px;line-height:28.5px}
.about p + p{margin-top:28px}
.grad-btn{background:linear-gradient(90deg,var(--navy-deep),var(--teal));box-shadow:0 4px 10px rgba(0,0,0,.25);border:2px solid var(--white);height:62px;font-size:18px}
.about .grad-btn{width:190px;margin-top:38px}

/* match */
.match{height:800px;text-align:center}
.match .section-title{width:840px;margin:0 auto;padding-top:95px;line-height:62px}
.match-cards{display:flex;gap:47px;justify-content:center;margin-top:106px}
.match-card{width:451px;height:407px;background:var(--white);border-radius:14px;box-shadow:0 4px 18px rgba(0,0,0,.12);overflow:hidden}
.match-photo{height:194px}
.match-card h3{font-family:'Poppins',sans-serif;font-weight:500;font-size:21px;line-height:26px;margin-top:22px;padding:0 20px}
.match-card .grad-btn{width:188px;margin-top:22px;font-size:18px}
.match-card .browse{display:block;margin-top:20px;font-family:'Poppins',sans-serif;font-weight:600;font-size:14px;color:var(--navy);text-decoration:none}

/* quote */
.quote{height:507px;position:relative;background:linear-gradient(90deg,#0d2d7a 0%,#1a4a9a 45%,#8ca6c8 62%,#c9c2b9 100%)}
.quote-photo{position:absolute;right:0;top:0;width:520px;height:100%;background:linear-gradient(135deg,#d8d2cb 0%,#c9b8a6 55%,#a88a6c 100%);opacity:.9}
.quote-copy{position:absolute;left:110px;top:66px;width:490px;color:var(--white)}
.quote-copy h2{font-family:'Poppins',sans-serif;font-weight:700;font-size:41px;margin-bottom:8px}
.quote-copy p{font-size:15px;font-weight:700;line-height:29.3px}
.quote-copy .btn-pill{margin-top:22px;width:190px;height:62px;border:2px solid var(--white);font-size:18px;background:var(--navy-deep)}

/* contact */
.contact{height:605px;text-align:center}
.contact .section-title{padding-top:58px}
.contact > p{width:770px;margin:22px auto 0;font-size:14.5px;line-height:30px}
.form{width:870px;margin:40px auto 0;display:grid;grid-template-columns:repeat(3,1fr);gap:15px 10px}
.field{height:50px;background:var(--white);box-shadow:0 2px 8px rgba(0,0,0,.13);text-align:left;padding:16px 17px;font-size:14px;color:#555}
.field.message{grid-column:1/4;height:93px}
.contact .grad-btn{width:174px;margin-top:56px}

/* footer */
.footer{height:311px;background:var(--teal);color:var(--white);position:relative}
.footer-brand{position:absolute;left:113px;top:60px;font-family:'Poppins',sans-serif;font-weight:700;font-size:28px;display:flex;align-items:center;gap:12px;width:300px;line-height:34px}
.footer-brand .brand-mark{background:var(--white);width:48px;height:48px}
.footer-col{position:absolute;top:50px}
.footer-col h4{font-family:'Poppins',sans-serif;font-weight:500;font-size:18px;letter-spacing:1px;margin-bottom:14px}
.footer-col a{display:block;color:var(--white);text-decoration:none;font-size:15px;line-height:34px;padding-left:6px}
.contact-line{display:flex;align-items:flex-start;gap:12px;font-size:15px;line-height:28px;margin-bottom:14px}
.contact-line svg{flex:none}
.copyright{height:79px;background:var(--teal-dark);color:var(--white);display:flex;align-items:center;justify-content:center;font-weight:700;font-size:15px}
</style>
</head>
<body>

<header>
  <div class="topbar">
    <span><svg width="13" height="13" viewBox="0 0 24 24" fill="#fff"><path d="M6.6 10.8a15 15 0 0 0 6.6 6.6l2.2-2.2c.3-.3.7-.4 1-.2 1.1.4 2.3.6 3.6.6.6 0 1 .4 1 1V20c0 .6-.4 1-1 1A17 17 0 0 1 3 4c0-.6.4-1 1-1h3.5c.6 0 1 .4 1 1 0 1.3.2 2.5.6 3.6.1.3 0 .7-.2 1z"/></svg>Call : (555) 310-2748</span>
    <span><svg width="14" height="11" viewBox="0 0 24 18" fill="#fff"><path d="M0 0h24v2L12 10 0 2z M0 4l12 8 12-8v14H0z"/></svg>Email : info@vellharborinsurance.example</span>
  </div>
  <nav class="nav">
    <div class="nav-links"><a class="active" href="#">Home</a><a href="#">About</a><a href="#">Get A Quote</a></div>
    <div class="brand"><span class="brand-mark"></span>Vell Harbor Insurance, LP</div>
    <a class="btn-pill contact-btn" href="#">Contact Us</a>
  </nav>
</header>

<section class="hero">
  <h1>At Vell Harbor Insurance, we understand that your peace of mind is invaluable.</h1>
</section>
<section class="split">
  <div class="split-card business">
    <div class="avatar"><div role="img" aria-label="Portrait of a smiling business woman" style="background:linear-gradient(160deg,#c98a5a,#b8571f)"></div></div>
    <div class="split-body">
      <h2>Business Insurance</h2>
      <p>General Liability&nbsp; Commercial<br>Auto Property Workers' Comp and much more</p>
      <a class="btn-pill" href="#">Find Business Insurance</a>
    </div>
  </div>
  <div class="split-card personal">
    <div class="split-body">
      <h2>Personal Insurance</h2>
      <p>General Liability&nbsp; Commercial<br>Auto Property Workers' Comp and much more</p>
      <a class="btn-pill" href="#">Find Personal Insurance</a>
    </div>
    <div class="avatar"><div role="img" aria-label="Photo of a couple reviewing a laptop" style="background:linear-gradient(160deg,#d9dde2,#6b7580)"></div></div>
  </div>
</section>
<div class="hero-tail"></div>

<section class="partners" aria-label="Carrier partners">
  <span class="partner">Dranko</span>
  <span class="partner">Lisk</span>
  <span class="partner">Corvane Mutual</span>
  <span class="partner">Tremix</span>
  <span class="partner">Wendmarch</span>
  <span class="partner">QRZ</span>
  <span class="partner">Plumeworth</span>
</section>

<section class="about">
  <div class="dash-right"></div>
  <h2 class="section-title">About Vell Harbor Insurance LP</h2>
  <p>Vell Harbor Insurance is a full-service, independent insurance agency with over three decades of experience in delivering comprehensive insurance solutions to individuals. We proudly offer a diverse portfolio of products from more than 20 of the most reputable and financially secure companies in the industry.</p>
  <p>Our dedicated team of over 50 skilled professionals is committed to customizing these products and services to meet the unique needs of each client. At Vell Harbor Insurance, our experts are focused on addressing the individual needs of our clients, ensuring exceptional service and support at every step.</p>
  <a class="btn-pill grad-btn" href="#">Read More</a>
  <div class="dash-left"></div>
</section>

<section class="match">
  <h2 class="section-title">Which insurance company is the best match for your needs?</h2>
  <div class="match-cards">
    <article class="match-card">
      <div class="match-photo" role="img" aria-label="Photo of a confident business woman in a yellow blazer" style="background:linear-gradient(135deg,#0c2a6e,#1a4a9e 55%,#c9a23a)"></div>
      <h3>Business Insurance Companies</h3>
      <a class="btn-pill grad-btn" href="#" style="background:var(--navy-deep)">Get Matched</a>
      <a class="browse" href="#">Or, browse all Business Insurance Companies</a>
    </article>
    <article class="match-card">
      <div class="match-photo" role="img" aria-label="Photo of a smiling man in a dark suit" style="background:linear-gradient(135deg,#0f6b4a,#17915f 50%,#2c3444)"></div>
      <h3>Home, Auto and Personal Insurance Companies</h3>
      <a class="btn-pill grad-btn" href="#" style="background:var(--navy-deep)">Get Matched</a>
      <a class="browse" href="#">Or, browse all Business Insurance Companies</a>
    </article>
  </div>
</section>

<section class="quote">
  <div class="quote-photo" role="img" aria-label="Photo of a hand holding a red umbrella over a small wooden house"></div>
  <div class="quote-copy">
    <h2>Get a Quote</h2>
    <p>We believe that securing your home is one of the most important decisions you can make. Obtaining a comprehensive insurance quote is essential to understanding your coverage options and ensuring that your property is adequately protected against unforeseen events. Our team of experienced professionals is here to guide you through the process, helping you find the right policy that meets your specific needs and budget. Don't leave your home's safety to chance—get a quote today and take the first step towards peace of mind.</p>
    <a class="btn-pill" href="#">Read More</a>
  </div>
</section>

<section class="contact">
  <h2 class="section-title">Get in Touch With Us</h2>
  <p>With our comprehensive range of insurance solutions, we are dedicated to safeguarding your assets and providing you with the security you deserve.</p>
  <form class="form">
    <div class="field">Name</div>
    <div class="field">Email</div>
    <div class="field">Phone Number</div>
    <div class="field message">Message</div>
  </form>
  <a class="btn-pill grad-btn" href="#">Submit</a>
</section>

<footer>
  <div class="footer">
    <div class="footer-brand"><span class="brand-mark"></span>Vell Harbor Insurance, LP</div>
    <div class="footer-col" style="left:446px">
      <h4>QUICK LINKS</h4>
      <a href="#">Home</a><a href="#">About</a><a href="#">Get a Quote</a>
    </div>
    <div class="footer-col" style="left:639px">
      <h4>HELP LINKS</h4>
      <a href="#">FAQ</a><a href="#">Terms of use</a><a href="#">Privacy Policy</a><a href="#">Support Links</a><a href="#">Conditions</a>
    </div>
    <div class="footer-col" style="left:835px">
      <h4>CONTACT US</h4>
      <div class="contact-line"><svg width="32" height="32" viewBox="0 0 32 32"><circle cx="16" cy="16" r="16" fill="#fff"/><path d="M16 8a5 5 0 0 0-5 5c0 4 5 10 5 10s5-6 5-10a5 5 0 0 0-5-5zm0 7a2 2 0 1 1 0-4 2 2 0 0 1 0 4z" fill="#1fa58a"/></svg><span>Vell Harbor Insurance LP.<br>United States</span></div>
      <div class="contact-line"><svg width="32" height="32" viewBox="0 0 32 32"><circle cx="16" cy="16" r="16" fill="#fff"/><path d="M12.5 14.5a10 10 0 0 0 5 5l1.6-1.6c.2-.2.5-.3.8-.2.8.3 1.7.4 2.6.4v3c0 .4-.3.7-.7.7A12 12 0 0 1 10 10.1c0-.4.3-.7.7-.7h3c0 .9.1 1.8.4 2.6.1.3 0 .6-.2.8z" fill="#1fa58a"/></svg><span>(555) 310-2748</span></div>
      <div class="contact-line"><svg width="32" height="32" viewBox="0 0 32 32"><circle cx="16" cy="16" r="16" fill="#fff"/><path d="M9 11h14v1.5L16 17l-7-4.5zM9 14l7 4.5 7-4.5v7H9z" fill="#1fa58a"/></svg><span>info@vellharborinsurance.example</span></div>
    </div>
  </div>
  <div class="copyright">Copyrights@2025.Vell Harbor Insurance LP.All Rights Reserved</div>
</footer>

</body>
</html>
```